Web Design Project - ReelHarbor Style Website

Hi there, we want to create a ReelHarbor / Flickden style website. We have a logo, and will be using a similar structure to this platform; http://tapecrate.example/v2/
Please feel free to be creative as possible, and make the site look however you would like :) keeping in mind the Ad space, and user friendly layout. We would like
1) The main page and
2) the video view page
designed
Updates
Logo and stock image uploaded
Hello; we most likely be basing the site on this tape crate theme, which also works as a mobile version.
Another option that I found for a layout which is different :)
http://www.quillnest-studio.example/demo-theme.cfm?theme=marvane
One last update; really like this one too
I am 100% likely to now use this format;
Target Market(s)
Bars, Cafe's, Restaurants, Attractions, Venues, Pubs, Wine and Dine
Industry/Entity Type
Reelharbor
Requirements
Must have
- Can be similar to ReelHarbor, but closer to Flickden's funky fresh look.
Should not have
- Not be too cluttered with too many videos on the home page. Feel free to think outside the box

```html
<!DOCTYPE html>
<html lang="en">
<head>
<meta charset="utf-8">
<title>Bayside Reels – Video View</title>
<link href="https://fonts.googleapis.com/css2?family=Questrial&family=Open+Sans:wght@300;400;600&display=swap" rel="stylesheet">
<style>
  :root{
    --page-bg:#121212;
    --accent:#2fd0f2;
    --rule-blue:#0f3d7a;
    --nav-bg:#1e1e1e;
    --nav-text:#d6d6d6;
    --strip-bg:#1c1c1c;
    --thumb-bg:#0b0b0b;
    --panel-bg:#f1f1f1;
    --title-blue:#4a6d94;
    --body-text:#4a4a4a;
    --muted-text:#8a8a8a;
    --ad-bg:#e6e6e6;
    --ad-text:#a9a9a9;
  }
  *{box-sizing:border-box;margin:0;padding:0}
  html,body{width:1200px;height:1194px;overflow:hidden;background:var(--page-bg);font-family:"Open Sans",sans-serif}
  .canvas{position:relative;width:1200px;height:1194px}
  .top-bar{position:absolute;left:0;top:0;width:1200px;height:4px;background:var(--accent)}
  .brand{position:absolute;left:218px;top:30px;display:flex;align-items:center;gap:10px;
    font-family:"Questrial",sans-serif;font-size:44px;color:var(--accent);letter-spacing:-1px}
  .brand-dot{width:22px;height:22px;border-radius:50%;background:var(--accent)}
  .blue-rule{position:absolute;left:218px;top:113px;width:740px;height:3px;background:var(--rule-blue)}
  .main-nav{position:absolute;left:206px;top:117px;width:764px;height:49px;background:var(--nav-bg)}
  .main-nav ul{list-style:none;position:absolute;left:23px;top:15px;display:flex;gap:18.5px;
    font-family:"Questrial",sans-serif;font-size:12.5px;color:var(--nav-text)}
  .main-nav li.is-active{color:var(--accent);font-weight:700}
  .search{position:absolute;left:595px;top:16px;width:153px;height:17px;display:flex}
  .search-field{flex:1;background:linear-gradient(#f6f6f6,#dcdcdc);font-size:8px;color:#999;padding:3px 4px;border:1px solid #888}
  .search-go{width:18px;background:var(--accent);display:flex;align-items:center;justify-content:center}
  .hero{position:absolute;left:218px;top:166px;width:740px;height:346px;
    background:radial-gradient(ellipse at 60% 60%,#f2b33a 0%,#d3398f 22%,#2fa0c8 45%,#1c4fc0 70%,#0e1f8a 100%)}
  .play-btn{position:absolute;left:569px;top:309px;width:50px;height:50px;border-radius:50%;background:rgba(255,255,255,.92)}
  .strip{position:absolute;left:206px;top:514px;width:764px;height:70px;background:var(--strip-bg)}
  .strip .thumb{position:absolute;top:11px;width:74px;height:50px;background:var(--thumb-bg)}
  .strip .arrow{position:absolute;top:24px}
  .content{position:absolute;left:218px;top:584px;width:740px;height:598px;background:var(--panel-bg)}
  .video-title{position:absolute;left:32px;top:22px;font-size:14.5px;font-weight:600;color:var(--title-blue)}
  .meta{position:absolute;left:32px;top:43px;font-size:7.5px;color:#333}
  .desc{position:absolute;left:32px;top:55px;width:405px;font-size:9.8px;line-height:12.5px;color:var(--muted-text);font-weight:300}
  .share{position:absolute;left:32px;top:113px;display:flex;gap:2.5px}
  .share span{width:12px;height:12px;border-radius:2px}
  .comments-head{position:absolute;left:32px;top:150px;font-size:11px;color:var(--title-blue);font-weight:300}
  .avatar{position:absolute;left:32px;top:168px;width:41px;height:41px;background:linear-gradient(#6b4a36,#c89776)}
  .comment-box{position:absolute;left:86px;top:167px;width:310px;height:42px;background:#fff;border:1px solid #ddd;font-size:7.5px;color:#aaa;padding:3px 9px}
  .comment{position:absolute;left:32px;width:380px;font-size:8.2px;line-height:10.7px;color:var(--body-text);font-weight:300}
  .comment .by{margin-top:4px;color:#666;font-size:7.3px}
  .comment .by span{margin-left:12px}
  .ad-space{position:absolute;left:500px;top:21px;width:218px;height:134px;background:var(--ad-bg);
    display:flex;align-items:center;justify-content:center;font-size:14px;color:var(--ad-text);font-weight:300}
  .related{position:absolute;left:500px;width:240px;height:51px}
  .related .pic{position:absolute;left:0;top:0;width:75px;height:51px;background:linear-gradient(#1c1c12,#5a5a44 70%,#2a2a1c)}
  .related .pic i{position:absolute;left:31px;top:19px;width:13px;height:13px;border-radius:50%;background:rgba(255,255,255,.85)}
  .related .txt{position:absolute;left:80px;top:1px;width:130px;font-size:8.2px;line-height:10.7px;color:#444;font-weight:300}
  .related .sub{margin-top:3px;font-size:7.2px;line-height:9.6px;color:#555}
</style>
</head>
<body>
<div class="canvas">
  <div class="top-bar"></div>
  <div class="brand"><span class="brand-dot"></span>Bayside Reels</div>
  <div class="blue-rule"></div>

  <nav class="main-nav">
    <ul>
      <li class="is-active">Home</li><li>My Channel</li><li>Likes</li><li>Videos</li>
      <li>Watch Later</li><li>TV Shows</li><li>Movies</li><li>Upload</li>
    </ul>
    <div class="search">
      <div class="search-field">search</div>
      <div class="search-go"><svg width="11" height="11" viewBox="0 0 11 11"><circle cx="5.5" cy="5.5" r="5" fill="#fff"/><path d="M4 3l3.5 2.5L4 8z" fill="#2fd0f2"/></svg></div>
    </div>
  </nav>

  <div class="hero" role="img" aria-label="Featured video still: colourful abstract swirls, triangles and bubbles on a blue background"></div>
  <svg class="play-btn" viewBox="0 0 50 50"><path d="M20 15l15 10-15 10z" fill="#2a5fc0"/></svg>

  <div class="strip">
    <svg class="arrow" style="left:8px" width="12" height="22" viewBox="0 0 12 22"><path d="M10 2L3 11l7 9" stroke="#555" stroke-width="3" fill="none"/></svg>
    <div class="thumb" style="left:26px"></div><div class="thumb" style="left:117px"></div>
    <div class="thumb" style="left:208px"></div><div class="thumb" style="left:299px"></div>
    <div class="thumb" style="left:390px"></div><div class="thumb" style="left:481px"></div>
    <div class="thumb" style="left:572px"></div><div class="thumb" style="left:663px"></div>
    <svg class="arrow" style="left:746px" width="12" height="22" viewBox="0 0 12 22"><path d="M2 2l7 9-7 9" stroke="#555" stroke-width="3" fill="none"/></svg>
  </div>

  <main class="content">
    <h1 class="video-title">Video Title</h1>
    <p class="meta">Published on May 23, 2012 by lumenpierfilms</p>
    <p class="desc">This is Pixelmoor's version&nbsp; of Lorem Ipsum. Proin gravida nibh vel velit auctor aliquet. Aenean sollicitudin, lorem quis bibendum auctor, nisi elit consequat ipsum, nec sagittis sem nibh id elit. Duis sed odio sit amet nibh vulputate cursus a sit amet mauris. Morbi accumsan ipsum velit. Nam nec tellus a odio tincidunt&nbsp; que.</p>
    <div class="share">
      <span style="background:#f08a24"></span><span style="background:#f5a623"></span><span style="background:#3b5fa8"></span>
      <span style="background:#e8c33a"></span><span style="background:#3aa8e0"></span><span style="background:#e8408a"></span>
    </div>

    <h2 class="comments-head">All Comments (37)</h2>
    <div class="avatar" role="img" aria-label="Commenter profile photo"></div>
    <div class="comment-box">Add a Comment</div>

    <div class="comment" style="top:224px">This is Pixelmoor's version&nbsp; of Lorem Ipsum. Proin gravida nibh vel velit auctor aliquet. Aenean sollicitudin, lorem quis bibendum auctor, nisi elit consequat ipsum, nec sagittis sem nibh id elit. Duis sed odio sit amet nibh vulputate cursus a sit amet mauris. Morbi accumsan ipsum velit.
      <div class="by">user124asdf<span>1 hour ago</span></div></div>
    <div class="comment" style="top:279px">Sed non&nbsp; mauris vitae erat consequat auctor eu in elit. Class aptent taciti sociosqu ad litora torquent per conubia nostra, per inceptos himenaeos. Mauris in erat justo. Nullam ac urna eu felis dapibus condimentum sit amet a augue. Sed non neque elit. Sed ut imperdiet nisi. Proin condimentum fermentum nunc. Etiam pharetra, erat sed fermentum feugiat, velit mauris egestas quam, ut aliquam massa nisl quis neque. Suspendisse in orci enim.
      <div class="by">user124asdf<span>1 hour ago</span></div></div>
    <div class="comment" style="top:363px">This is Pixelmoor's version&nbsp; of Lorem Ipsum. Proin gravida nibh vel velit auctor aliquet. Aenean sollicitudin, lorem quis bibendum auctor, nisi elit consequat ipsum, nec sagittis sem nibh id elit. Duis sed odio sit amet nibh vulputate cursus a sit amet mauris. Morbi accumsan ipsum velit. auctor eu in elit.
      <div class="by">user124asdf<span>1 hour ago</span></div></div>

    <aside class="ad-space">space for ads</aside>

    <div class="related" style="top:164px"><div class="pic" role="img" aria-label="Video thumbnail: white tulips on dark background"><i></i></div><div class="txt">This is Pixelmoor's version&nbsp; of Lorem Ipsum.<div class="sub">uploaded by user2345<br>34,342 views</div></div></div>
    <div class="related" style="top:224px"><div class="pic" role="img" aria-label="Video thumbnail: white tulips on dark background"><i></i></div><div class="txt">This is Pixelmoor's version&nbsp; of Lorem Ipsum.<div class="sub">uploaded by user2345<br>34,342 views</div></div></div>
    <div class="related" style="top:284px"><div class="pic" role="img" aria-label="Video thumbnail: white tulips on dark background"><i></i></div><div class="txt">This is Pixelmoor's version&nbsp; of Lorem Ipsum.<div class="sub">uploaded by user2345<br>34,342 views</div></div></div>
    <div class="related" style="top:344px"><div class="pic" role="img" aria-label="Video thumbnail: white tulips on dark background"><i></i></div><div class="txt">This is Pixelmoor's version&nbsp; of Lorem Ipsum.<div class="sub">uploaded by user2345<br>34,342 views</div></div></div>
    <div class="related" style="top:404px"><div class="pic" role="img" aria-label="Video thumbnail: white tulips on dark background"><i></i></div><div class="txt">This is Pixelmoor's version&nbsp; of Lorem Ipsum.<div class="sub">uploaded by user2345<br>34,342 views</div></div></div>
    <div class="related" style="top:464px"><div class="pic" role="img" aria-label="Video thumbnail: white tulips on dark background"><i></i></div><div class="txt">This is Pixelmoor's version&nbsp; of Lorem Ipsum.<div class="sub">uploaded by user2345<br>34,342 views</div></div></div>
    <div class="related" style="top:524px"><div class="pic" role="img" aria-label="Video thumbnail: white tulips on dark background"><i></i></div><div class="txt">This is Pixelmoor's version&nbsp; of Lorem Ipsum.<div class="sub">uploaded by user2345<br>34,342 views</div></div></div>
  </main>
</div>
</body>
</html>
```